Book Cover Design - Uncovering Weight Loss Secrets

I need a book cover design for a book called 'Folding The Map'. It is a book that goes through all of the secrets to weight loss, without any crazy shakes or workouts or pills or potions. The book is really focused on helping people understand that Weight loss is simple and has more to do with our mindset as well as the food we were eating. It is about taking personal responsibility not looking for the next fancy revolutionary product that is going to help them magically melt the fat away. The book is pragmatic in nature and breaks down in simple terms how we can lose weight and keep it off for the rest of our lives. It shows the user that it is simple to lose weight, but it takes effort. They should stop looking for a quick fix when it comes to weight loss but instead eat healthy for the rest of their lives.
The book is intended to be hard-hitting no holds barred approach. The book has the same title as my business name. I will attach the current logo that we use in the business. This doesn't need to be on the front of the book maybe at the back down the bottom somewhere.
I am looking to have both an e-book cover and a standard printed book cover.
I don't have any colours in mind, my logo can be adapted to be different colours or just white.
The message that I am wanting people to feel when they see my book, is that all these Weightloss fads are a joke, that I know the secrets that will get them to their weight loss goal even if they fail at everything else before.
On the cover it should say the following.
FOLDING THE MAP
Uncovering the Weight Loss Secrets
The big companies have been trying to keep hidden for years!
COLIN MAYHEW
People who have failed many times trying to lose weight & need help
Weight Loss

```html
<!DOCTYPE html>
<html lang="en">
<head>
<meta charset="utf-8">
<title>Folding The Map — Book Cover</title>
<link rel="stylesheet" href="https://fonts.googleapis.com/css2?family=Lato:ital,wght@0,400;0,700;1,700&display=swap">
<style>
  :root {
    --backdrop: #dcdcdc;
    --cover-white: #ffffff;
    --ink: #2f2f3a;
    --gold: #a88a55;
    --apple-red: #c0603a;
    --apple-green: #c9c46a;
    --tape-white: #eeeeea;
  }
  * { margin: 0; padding: 0; box-sizing: border-box; }
  html, body {
    width: 1200px;
    height: 1200px;
    overflow: hidden;
    background: var(--backdrop);
  }
  .cover {
    position: absolute;
    left: 240px;
    top: 60px;
    width: 720px;
    height: 1080px;
    background: var(--cover-white);
    font-family: "Lato", sans-serif;
    color: var(--ink);
    text-align: center;
  }
  .cover-title {
    position: absolute;
    top: 90px;
    left: 0;
    width: 100%;
    font-weight: 400;
    font-size: 112px;
    line-height: 134px;
    letter-spacing: 1px;
  }
  .cover-subtitle {
    position: absolute;
    top: 360px;
    left: 0;
    width: 100%;
    font-weight: 700;
    font-size: 26px;
    letter-spacing: 5px;
    color: var(--gold);
  }
  .cover-tagline {
    position: absolute;
    top: 405px;
    left: 0;
    width: 100%;
    font-size: 23px;
    line-height: 30px;
  }
  .cover-tagline .emphasis {
    font-weight: 700;
    font-style: italic;
  }
  .cover-artwork {
    position: absolute;
    top: 510px;
    left: 0;
    width: 720px;
    height: 470px;
  }
  .cover-author {
    position: absolute;
    top: 965px;
    left: 0;
    width: 100%;
    font-size: 52px;
    font-weight: 400;
    letter-spacing: 1px;
  }
</style>
</head>
<body>
  <main class="cover">
    <h1 class="cover-title">FOLDING<br>THE MAP</h1>
    <p class="cover-subtitle">WEIGHT LOSS SECRETS</p>
    <p class="cover-tagline">
      For Losing all the Weight<br>
      You Want &amp; Keeping it off Forever<br>
      <span class="emphasis">No Matter What You Have Tried in The Past</span>
    </p>
    <svg class="cover-artwork" viewBox="0 0 720 470" role="img" aria-label="Photograph of a red and green apple with a zipper opened down its front, wrapped at its base by a curving measuring tape">
      <defs>
        <radialGradient id="apple-tone" cx="50%" cy="42%" r="50%">
          <stop offset="0" stop-color="var(--apple-green)"/>
          <stop offset="0.45" stop-color="var(--apple-red)"/>
          <stop offset="0.8" stop-color="#e9c9b8" stop-opacity="0.6"/>
          <stop offset="1" stop-color="#ffffff" stop-opacity="0"/>
        </radialGradient>
        <linearGradient id="tape-tone" x1="0" y1="0" x2="1" y2="0">
          <stop offset="0" stop-color="#ffffff"/>
          <stop offset="0.5" stop-color="var(--tape-white)"/>
          <stop offset="1" stop-color="#ffffff"/>
        </linearGradient>
      </defs>
      <rect width="720" height="470" fill="url(#tape-tone)"/>
      <ellipse cx="360" cy="230" rx="230" ry="210" fill="url(#apple-tone)"/>
    </svg>
    <p class="cover-author">COLIN MAYHEW</p>
  </main>
</body>
</html>
```